Fresh and unique Mortgage Broking business needs website design.

We need a professional yet fresh, bright and colourful website for my Mortgage broking business.
We specialise in the Non conforming/sub prime market with clients who have been rejected by other banks or have trouble getting finance through a traditional lender.
We are called Brightwell Lending and we aim to provide Hope to our clients when they have thought there was no hope.
I would like it to be on a Wordpress platform as I plan to do a lot of postings, both written and video and I need it to be easy to use.
I would also like it to be able to have a clear and simple enquiry box on the first page to capture contact details and notify me via email.

I have already had the logo designed in both green and black and a white version.
I have also had a a header made up using the white logo with leaves background that could possibly be used as the website header which I have used as my facebook header.

https://www.facebook.com/MarcusTolvenBright/

I tried playing around with a jimdo website builder which kind of got some of the brightness and colours I was after but it had a lot to go.

http://brightwelllending.sitevale.example/

Industry/Entity Type

Finance

Number of Pages Required

4 page

Colors
0292cd
00a990
fbed22
ffc214
f78f20
ec1f27

Requirements
Nice to have
• I'm not sure what the difference between uncoded and coded website is so I'm not sure what I need?

```html
<!DOCTYPE html>
<html lang="en">
<head>
<meta charset="utf-8">
<title>Brightwell Lending</title>
<link rel="stylesheet" href="https://fonts.googleapis.com/css2?family=Mulish:wght@400;600;700&family=Open+Sans:wght@400;600&display=swap">
<style>
:root{
  --green:#0e7a3c;
  --blue:#0292cd;
  --teal:#00a990;
  --yellow:#ffc214;
  --orange:#f78f20;
  --red:#ec1f27;
  --ink:#333333;
  --muted:#8a8a8a;
  --light:#f0f0f0;
  --white:#ffffff;
}
*{box-sizing:border-box;margin:0;padding:0}
html,body{width:1200px;height:2761px;overflow:hidden}
body{position:relative;background:var(--white);font-family:"Open Sans",Arial,sans-serif;color:var(--ink)}
.abs{position:absolute}
.heading{font-family:"Mulish",Arial,sans-serif}

/* header */
.site-header{top:0;left:0;width:1200px;height:122px;background:var(--white)}
.brand{left:128px;top:38px;display:flex;align-items:center;gap:12px;font-family:"Mulish",Arial,sans-serif;font-weight:700;font-size:30px;color:var(--green)}
.brand-dot{width:22px;height:22px;border-radius:50%;background:var(--green)}
.main-nav{top:73px;left:476px;display:flex;gap:0;font-family:"Mulish",Arial,sans-serif;font-size:16px;font-weight:600;color:#444}
.main-nav a{color:inherit;text-decoration:none;margin-right:36px}
.main-nav a.active{color:var(--green)}

/* hero */
.hero{top:122px;left:0;width:1200px;height:514px;background:
  radial-gradient(circle at 32% 45%,#f6a22a 0,#e0671a 22%,transparent 48%),
  radial-gradient(circle at 75% 35%,#f28a22 0,#d4481a 25%,transparent 55%),
  radial-gradient(circle at 50% 85%,#9aa63a 0,transparent 45%),
  linear-gradient(90deg,#b8451c 0%,#e98226 40%,#c8561a 70%,#5a2010 100%)}
.hero-title{top:290px;left:0;width:1200px;text-align:center;color:var(--white);font-size:52px;font-weight:600;letter-spacing:.5px}
.hero-sub{top:352px;left:0;width:1200px;text-align:center;color:var(--white);font-size:32px;font-weight:600}
.hero-btn{top:411px;left:486px;width:220px;height:44px;border:2px solid var(--white);color:var(--white);font-size:18px;font-weight:700;display:flex;align-items:center;justify-content:center}
.dots{top:588px;left:554px;display:flex;gap:8px}
.dots span{width:15px;height:15px;border-radius:50%;background:var(--white)}
.dots span.current{background:transparent;border:2px solid var(--white)}

/* services */
.intro-title{top:684px;left:0;width:1200px;text-align:center;font-size:30px;line-height:37px;color:#333;font-weight:400}
.intro-text{top:776px;left:190px;width:820px;text-align:center;font-size:13px;line-height:25px;color:var(--muted)}
.service{top:852px;width:300px;text-align:center}
.service svg{display:block;margin:0 auto}
.service h3{margin-top:22px;font-family:"Mulish",Arial,sans-serif;font-weight:400;font-size:21px;color:#222}
.service p{margin-top:8px;font-size:12.5px;line-height:21px;color:var(--muted);padding:0 20px}
.slide-arrow{top:945px}

/* why band */
.why{top:1192px;left:0;width:1200px;height:455px;background:linear-gradient(90deg,#f4f7fa 0%,#e6eef4 50%,#eef3f7 100%);border-top:1px solid #e2e6ea;border-bottom:1px solid #e2e6ea}
.why-photo{top:1192px;left:440px;width:495px;height:455px;background:linear-gradient(135deg,#dfe8ef 0%,#c9a58c 35%,#8a6a55 60%,#2f5f86 100%)}
.why-kicker{top:1265px;left:118px;color:var(--teal);font-family:"Mulish",Arial,sans-serif;font-size:22px}
.why-title{top:1302px;left:118px;color:#555;font-family:"Mulish",Arial,sans-serif;font-size:34px;font-weight:700}
.why-text{top:1356px;left:118px;width:340px;font-size:13px;line-height:27px;color:var(--muted)}
.btn-teal{top:1502px;left:116px;width:131px;height:38px;background:var(--teal);color:var(--white);font-size:14px;display:flex;align-items:center;justify-content:center}
.enquiry{top:1235px;left:760px;width:326px;height:362px;background:var(--white);border:1px solid #dde2e6;box-shadow:0 2px 6px rgba(0,0,0,.08)}
.enquiry h2{position:absolute;top:24px;left:26px;font-family:"Mulish",Arial,sans-serif;font-size:23px;font-weight:700;color:var(--red)}
.field{position:absolute;left:26px;width:276px;height:38px;border:1px solid #c9cdd1;display:flex;align-items:center;gap:8px;padding-left:10px;font-size:12px;color:#555}
.field.message{height:76px;align-items:flex-start;padding-top:10px}
.submit{position:absolute;left:26px;top:298px;width:276px;height:42px;background:var(--red);color:var(--white);font-family:"Mulish",Arial,sans-serif;font-weight:700;font-size:18px;display:flex;align-items:center;justify-content:center}

/* property */
.property-photo{top:1717px;left:125px;width:403px;height:248px;background:linear-gradient(180deg,#5c7fae 0%,#8aa6c8 40%,#b9b2a6 65%,#5e7a3e 100%)}
.property-title{top:1714px;left:570px;font-family:"Mulish",Arial,sans-serif;font-size:28px;color:#555}
.property-text{left:570px;width:500px;font-size:12.5px;line-height:26px;color:var(--muted)}
.btn-orange{top:1928px;left:574px;width:134px;height:40px;background:var(--orange);color:var(--white);font-size:14px;display:flex;align-items:center;justify-content:center}

/* testimonials */
.testimonials{top:2043px;left:0;width:1200px;height:355px;background:linear-gradient(110deg,#fbbd14 0%,#f5c31a 25%,#93be3a 55%,#1ba883 80%,#00a990 100%)}
.testi-title{top:2100px;left:0;width:1180px;text-align:center;color:var(--white);font-family:"Mulish",Arial,sans-serif;font-size:28px}
.client-photo{top:2151px;left:270px;width:180px;height:180px;border-radius:50%;border:5px solid var(--white);background:linear-gradient(160deg,#9a5a3e 0%,#6a3e55 55%,#3e2a48 100%)}
.quote{top:2172px;left:478px;width:520px;color:var(--white);font-size:17px;line-height:29px}
.quote .mark{font-family:Georgia,serif;font-size:48px;line-height:0;vertical-align:-16px}
.author{top:2282px;left:480px;color:var(--white);font-size:16px}

/* footer */
.site-footer{top:2398px;left:0;width:1200px;height:363px;background:var(--light)}
.foot-title{font-family:"Mulish",Arial,sans-serif;font-size:24px;color:#333}
.foot-list{list-style:none;font-size:13px;line-height:28px;color:#666}
.contact-line{font-size:13px;line-height:27px;color:#555;display:flex;align-items:center;gap:10px}
.socials{top:2498px;left:802px;display:flex;gap:11px}
.socials span{width:36px;height:36px;border-radius:50%;background:var(--teal)}
.foot-rule{top:2702px;left:112px;width:978px;height:1px;background:#d8d8d8}
.copyright{top:2716px;left:0;width:1200px;text-align:center;font-size:12px;color:#666}
</style>
</head>
<body>

<header class="site-header abs">
  <div class="brand abs"><span class="brand-dot"></span>Brightwell Lending</div>
  <nav class="main-nav abs">
    <a class="active" href="#">HOME</a>
    <a href="#">ABOUT US</a>
    <a href="#">SERVICES</a>
    <a href="#">PROPERTY ADVICE</a>
    <a href="#">CONTACT</a>
  </nav>
</header>

<section class="hero abs" role="img" aria-label="Close-up of orange autumn maple leaves on a soft green background"></section>
<h1 class="hero-title heading abs">WE HELP YOU IN FINANCING</h1>
<p class="hero-sub heading abs">MAURIS VEL LACUS VITAE FELIS</p>
<div class="hero-btn heading abs">FREE QUOTE NOW</div>
<div class="dots abs"><span class="current"></span><span></span><span></span><span></span></div>

<h2 class="intro-title heading abs">HOPE FOR YOUR FINANCE WHEN<br>ALL HOPE IS LOST</h2>
<p class="intro-text abs">Curabitur iaculis tempus eros Curabitur vel mi sit amet magna malesuada ultrices Ut nisi erat fermentum vel congue id euismod in elit Fusce ultricies orci ac feugiat suscipit leo massa sodales velit et scelerisque mi tortor</p>

<svg class="slide-arrow abs" style="left:114px" width="24" height="60" viewBox="0 0 24 60"><polyline points="22,2 2,30 22,58" fill="none" stroke="#777" stroke-width="1.5"/></svg>
<svg class="slide-arrow abs" style="left:1050px" width="24" height="60" viewBox="0 0 24 60"><polyline points="2,2 22,30 2,58" fill="none" stroke="#777" stroke-width="1.5"/></svg>

<div class="service abs" style="left:154px">
  <svg width="156" height="168" viewBox="0 0 156 168">
    <polygon points="78,4 150,44 150,124 78,164 6,124 6,44" fill="none" stroke="#0292cd" stroke-width="2.5"/>
    <polygon points="78,14 141,49 141,119 78,154 15,119 15,49" fill="#0292cd"/>
    <g fill="none" stroke="#fff" stroke-width="3">
      <polyline points="44,82 78,56 112,82"/>
      <rect x="52" y="80" width="52" height="36"/>
      <rect x="60" y="92" width="16" height="24"/>
      <rect x="84" y="90" width="14" height="12"/>
    </g>
  </svg>
  <h3>Residential loans</h3>
  <p>Morbi porta libero id ullamcorper nonum my nibh ligula pulvinar</p>
</div>

<div class="service abs" style="left:453px">
  <svg width="156" height="168" viewBox="0 0 156 168">
    <polygon points="78,4 150,44 150,124 78,164 6,124 6,44" fill="none" stroke="#0292cd" stroke-width="2.5"/>
    <polygon points="78,14 141,49 141,119 78,154 15,119 15,49" fill="#0292cd"/>
    <path d="M40,78 Q78,36 116,78 Z" fill="#fff"/>
    <line x1="78" y1="78" x2="78" y2="92" stroke="#fff" stroke-width="3"/>
    <path d="M64,96 Q78,88 92,96 L96,122 Q78,128 60,122 Z" fill="none" stroke="#fff" stroke-width="3"/>
    <text x="78" y="117" text-anchor="middle" fill="#fff" font-family="Open Sans,sans-serif" font-size="18" font-weight="600">$</text>
  </svg>
  <h3>Investment loans</h3>
  <p>Morbi porta libero id ullamcorper nonum my nibh ligula pulvinar</p>
</div>

<div class="service abs" style="left:750px">
  <svg width="156" height="168" viewBox="0 0 156 168">
    <polygon points="78,4 150,44 150,124 78,164 6,124 6,44" fill="none" stroke="#0292cd" stroke-width="2.5"/>
    <polygon points="78,14 141,49 141,119 78,154 15,119 15,49" fill="#0292cd"/>
    <g fill="none" stroke="#fff" stroke-width="3">
      <circle cx="78" cy="62" r="11"/>
      <path d="M58,92 Q78,72 98,92"/>
      <rect x="50" y="92" width="56" height="30" rx="2"/>
      <line x1="42" y1="126" x2="114" y2="126"/>
    </g>
  </svg>
  <h3>Self Employed loans</h3>
  <p>Morbi porta libero id ullamcorper nonum my nibh ligula pulvinar</p>
</div>

<section class="why abs"></section>
<div class="why-photo abs" role="img" aria-label="Smiling young couple embracing"></div>
<p class="why-kicker abs">Pellentesque faucibus accum</p>
<h2 class="why-title abs">Why We Are</h2>
<p class="why-text abs">Curabitur iaculis tempus eros Curabitur vel mi sit amet magna malesuada ultrices Ut nisi erat fermentum vel congue id euismod in elit Fusce ultricies orci ac feugiat suscipit leo massa sodales velit et scelerisque mi tortor at ipsum cligula augue bibendum</p>
<div class="btn-teal abs">Learn More</div>

<form class="enquiry abs">
  <h2>Need a Loan or Advice</h2>
  <div class="field" style="top:80px"><svg width="13" height="13" viewBox="0 0 13 13"><circle cx="6.5" cy="4" r="3" fill="#999"/><path d="M1,13 Q6.5,5 12,13Z" fill="#999"/></svg>Name</div>
  <div class="field" style="top:127px"><svg width="14" height="10" viewBox="0 0 14 10"><rect width="14" height="10" fill="#999"/><polyline points="0,0 7,6 14,0" fill="none" stroke="#fff" stroke-width="1.2"/></svg>Email</div>
  <div class="field" style="top:174px"><svg width="13" height="13" viewBox="0 0 13 13"><path d="M3,1 L5,4 L4,6 Q6,9 8,9 L9,8 L12,10 L11,12 Q5,13 1,3 Z" fill="#999"/></svg>Phone</div>
  <div class="field message" style="top:220px">Message</div>
  <div class="submit">SUBMIT</div>
</form>

<div class="property-photo abs" role="img" aria-label="Two-storey family house at dusk"></div>
<h2 class="property-title abs">Property Advice</h2>
<p class="property-text abs" style="top:1762px">Morbi porta libero id ullamcorper nonummy nibh ligula pulvinar metus eget consectetuer augue nisi quis lacus Ut ac mi quis lacus</p>
<p class="property-text abs" style="top:1830px">mollis aliquam Curabitur iaculis tempus eros Curabitur vel mi sit amet magna malesuada ultrices Ut nisi erat fermentum vel congue id euismod in elit Fusce ultricies orci ac feugiat suscipit leo massa sodales</p>
<div class="btn-orange abs">Learn More</div>

<section class="testimonials abs"></section>
<h2 class="testi-title abs">Client Testimonials</h2>
<svg class="abs" style="left:174px;top:2206px" width="20" height="34" viewBox="0 0 20 34"><polyline points="17,3 4,17 17,31" fill="none" stroke="#fff" stroke-width="4"/></svg>
<svg class="abs" style="left:1016px;top:2206px" width="20" height="34" viewBox="0 0 20 34"><polyline points="3,3 16,17 3,31" fill="none" stroke="#fff" stroke-width="4"/></svg>
<div class="client-photo abs" role="img" aria-label="Portrait of a smiling client couple"></div>
<p class="quote abs"><span class="mark">&ldquo;</span> Donec dictum lectus non odio Cras a ante vitae enim iaculis aliquam Mauris nunc quam venenatis nec euismod sit amet egestas placerat est <span class="mark">&rdquo;</span></p>
<p class="author abs">By Author Name</p>

<footer class="site-footer abs"></footer>
<h3 class="foot-title abs" style="top:2456px;left:112px">Quick Links</h3>
<ul class="foot-list abs" style="top:2500px;left:115px"><li>Home</li><li>About us</li><li>Our Services</li><li>Why Us</li><li>FAQ</li></ul>
<ul class="foot-list abs" style="top:2510px;left:302px"><li>Testimonials</li><li>Locations</li><li>Blogs</li><li>Contact Us</li></ul>
<h3 class="foot-title abs" style="top:2454px;left:488px">Contact Us</h3>
<div class="abs" style="top:2498px;left:489px">
  <p class="contact-line">418 Meadowgate Road Suite 12</p>
  <p class="contact-line">Ashbury, PA 19920</p>
  <p class="contact-line" style="margin-top:6px"><svg width="14" height="14" viewBox="0 0 13 13"><path d="M3,1 L5,4 L4,6 Q6,9 8,9 L9,8 L12,10 L11,12 Q5,13 1,3 Z" fill="#f78f20"/></svg>(555) 318-4702</p>
  <p class="contact-line"><svg width="14" height="11" viewBox="0 0 14 10"><rect width="14" height="10" fill="#f78f20"/><polyline points="0,0 7,6 14,0" fill="none" stroke="#fff" stroke-width="1.2"/></svg>info@brightwelllending.example</p>
</div>
<h3 class="foot-title abs" style="top:2454px;left:806px">Follow Us</h3>
<div class="socials abs"><span></span><span></span><span></span><span></span><span></span></div>
<div class="foot-rule abs"></div>
<p class="copyright abs">&copy; 2016 Company Name&nbsp; All right reserved&nbsp; Term of Use</p>

</body>
</html>
```